NEW YORK Plumbing/utility company 10 year anniversary business card

Looking For simple back and front business card would like to include a few things in description
We offer 24/7 emergency service
residential
commercial
industrial
municipal
services offered
Plumbing
hydro excavation
hydro jetting
Well pumps
Sewer pumps
water mains
sewer mains

```html
<!DOCTYPE html>
<html lang="en">
<head>
<meta charset="utf-8">
<title>Crestline Water &amp; Sewer – Business Card</title>
<link href="https://fonts.googleapis.com/css2?family=Montserrat:wght@500;600;700;800&display=swap" rel="stylesheet">
<style>
  :root {
    --navy: #0a62a6;
    --navy-deep: #07548f;
    --sky: #35a8e0;
    --white: #ffffff;
    --drop-light: #eef2f5;
    --backdrop: #2b2c2e;
    --ink-muted: #0a62a6;
  }
  * { box-sizing: border-box; margin: 0; padding: 0; }
  html, body {
    width: 1200px; height: 801px; overflow: hidden;
    background: var(--backdrop);
    font-family: "Montserrat", Arial, sans-serif;
  }
  .stage {
    position: relative; width: 1200px; height: 801px;
    display: flex; align-items: center; justify-content: center; gap: 40px;
  }
  .card {
    position: relative; width: 560px; height: 320px;
    border-radius: 12px; overflow: hidden;
  }

  /* ---------- back side ---------- */
  .card--back { background: var(--navy); }
  .card--back .texture {
    position: absolute; inset: 0;
    background: radial-gradient(circle at 30% 40%, #1a78bd 0%, var(--navy) 70%);
  }
  .brand {
    position: absolute; display: flex; align-items: center; gap: 12px;
  }
  .brand__dot { width: 22px; height: 22px; border-radius: 50%; flex: none; }
  .brand__name {
    font-weight: 800; font-size: 26px; line-height: 1.1; letter-spacing: 0.5px;
    text-transform: uppercase;
  }
  .card--back .brand { left: 36px; top: 92px; width: 250px; }
  .card--back .brand__dot { background: var(--white); }
  .card--back .brand__name { color: var(--white); }

  .services {
    position: absolute; left: 300px; top: 36px; list-style: none;
    color: var(--white); font-weight: 700; font-size: 17px; line-height: 25px;
  }
  .services li { display: flex; align-items: center; gap: 8px; }
  .services li::before {
    content: ""; width: 7px; height: 7px; border-radius: 50%; background: var(--sky);
  }
  .sector-band {
    position: absolute; left: 0; right: 0; bottom: 22px; height: 38px;
    background: var(--sky); color: var(--white);
    display: flex; align-items: center; justify-content: center;
    font-weight: 700; font-size: 15px; letter-spacing: 1px;
  }
  .sector-band span.sep { margin: 0 10px; }

  /* ---------- front side ---------- */
  .card--front { background: var(--white); }
  .card--front .texture {
    position: absolute; inset: 0;
    background: radial-gradient(circle at 50% 45%, var(--white) 0%, var(--drop-light) 100%);
  }
  .card--front .brand { left: 34px; top: 100px; width: 230px; }
  .card--front .brand__dot { background: var(--navy); }
  .card--front .brand__name { color: var(--navy); }

  .divider {
    position: absolute; left: 282px; top: 48px; width: 1.5px; height: 162px;
    background: var(--navy);
  }
  .contact { position: absolute; left: 302px; top: 56px; }
  .contact__name {
    color: var(--sky); font-weight: 800; font-size: 24px; letter-spacing: 0.5px;
    text-transform: uppercase;
  }
  .contact__role {
    color: var(--navy); font-weight: 500; font-size: 14px; margin-top: 2px;
    padding-bottom: 10px; border-bottom: 1.5px solid var(--sky); width: 200px;
  }
  .contact__list { list-style: none; margin-top: 10px; }
  .contact__list li {
    display: flex; align-items: center; gap: 8px;
    color: var(--navy); font-weight: 500; font-size: 14px; line-height: 24px;
  }
  .contact__icon { width: 16px; height: 16px; flex: none; }

  .emergency-band {
    position: absolute; left: 0; right: 0; bottom: 22px; height: 44px;
    background: var(--navy); color: var(--white);
    display: flex; align-items: center; justify-content: center;
    font-weight: 800; font-size: 17px; letter-spacing: 0.5px; text-transform: uppercase;
  }
</style>
</head>
<body>
<main class="stage">

  <!-- Back side -->
  <section class="card card--back">
    <div class="texture" role="img" aria-label="Water droplets scattered across a blue surface"></div>
    <div class="brand">
      <span class="brand__dot"></span>
      <span class="brand__name">Crestline Water &amp; Sewer</span>
    </div>
    <ul class="services">
      <li>Plumbing</li>
      <li>Hydro Excavation</li>
      <li>Hydro Jetting</li>
      <li>Well Pumps</li>
      <li>Sewer Pumps</li>
      <li>Water Mains</li>
      <li>Sewer Mains</li>
    </ul>
    <div class="sector-band">
      RESIDENTIAL<span class="sep">|</span>COMMERCIAL<span class="sep">|</span>INDUSTRIAL<span class="sep">|</span>MUNICIPAL
    </div>
  </section>

  <!-- Front side -->
  <section class="card card--front">
    <div class="texture" role="img" aria-label="Clear water droplets scattered across a white surface"></div>
    <div class="brand">
      <span class="brand__dot"></span>
      <span class="brand__name">Crestline Water &amp; Sewer</span>
    </div>
    <div class="divider"></div>
    <div class="contact">
      <div class="contact__name">Dana Moreland</div>
      <div class="contact__role">Director</div>
      <ul class="contact__list">
        <li>
          <svg class="contact__icon" viewBox="0 0 16 16"><circle cx="8" cy="8" r="8" fill="#35a8e0"/><path d="M5.2 4.2l1.4-.2.8 1.8-.9.7a5 5 0 0 0 2.9 2.9l.7-.9 1.8.8-.2 1.4c-3.6.3-6.8-2.9-6.5-6.5z" fill="#fff"/></svg>
          555-014-2280
        </li>
        <li>
          <svg class="contact__icon" viewBox="0 0 16 16"><circle cx="8" cy="8" r="8" fill="#35a8e0"/><rect x="4" y="5.2" width="8" height="5.6" fill="#fff"/><path d="M4 5.4l4 3 4-3" stroke="#35a8e0" stroke-width="1" fill="none"/></svg>
          info@crestlinews.com
        </li>
        <li>
          <svg class="contact__icon" viewBox="0 0 16 16"><circle cx="8" cy="8" r="8" fill="#35a8e0"/><circle cx="8" cy="8" r="4" stroke="#fff" stroke-width="1" fill="none"/><path d="M4 8h8M8 4c-2 2.4-2 5.6 0 8M8 4c2 2.4 2 5.6 0 8" stroke="#fff" stroke-width="0.9" fill="none"/></svg>
          www.crestlinews.com
        </li>
      </ul>
    </div>
    <div class="emergency-band">We offer 24/7 emergency service</div>
  </section>

</main>
</body>
</html>
```